Business Card Design

Harlow Sun and Electrical is a new company that specializes in solar pv. I need a card with similar attributes to the ones I have attached. I am after a two sided card with the logo on one side and the logo plus info on the other. I would prefer one side to be black and the other to be a colour but am open to suggestions. The colour scheme I was thinking of was blue or green. I plan on spot glossing the logos if that makes any difference. I have attached a file of my logo in a few colours, none of which I am completely sold on so please feel free to change colous to suit.
Thanks.
Contact Information for Business Card
Dorian Harlow, www.hwx-example.net.nz, dorian@hwx-example.net.nz, t. 0508 4 BRIGHT m. 027469318

```html
<!DOCTYPE html>
<html lang="en">
<head>
<meta charset="utf-8">
<title>Harlow Sun and Electrical — Business Card</title>
<link rel="stylesheet" href="https://fonts.googleapis.com/css2?family=Lato:wght@300;400;700&display=swap">
<style>
  :root {
    --backdrop: #222222;
    --card-light: #f4f4f4;
    --card-shade: #e2e2e2;
    --brand-blue: #3a7fc1;
    --brand-blue-deep: #2f6eab;
    --label-blue: #2f62b8;
    --ink-dark: #333333;
    --ink-soft: #6b6b6b;
    --rule: #3a3a3a;
    --logo-ink: #ffffff;
  }
  * { box-sizing: border-box; margin: 0; padding: 0; }
  html, body {
    width: 1200px;
    height: 797px;
    overflow: hidden;
    background: var(--backdrop);
    font-family: "Lato", Arial, sans-serif;
  }
  .stage {
    width: 1200px;
    height: 797px;
    display: flex;
    align-items: center;
    justify-content: center;
  }
  .card {
    position: relative;
    width: 640px;
    height: 370px;
    border-radius: 4px;
    background: linear-gradient(160deg, var(--card-light) 0%, var(--card-shade) 100%);
    box-shadow: 0 14px 30px rgba(0,0,0,0.45);
    overflow: hidden;
  }
  .brand-tab {
    position: absolute;
    left: 95px;
    top: 0;
    width: 470px;
    height: 150px;
    border-radius: 0 0 14px 14px;
    background: linear-gradient(180deg, var(--brand-blue) 0%, var(--brand-blue-deep) 100%);
    display: flex;
    align-items: center;
    justify-content: center;
  }
  .brand-name {
    color: var(--logo-ink);
    font-weight: 400;
    font-size: 34px;
    letter-spacing: 1px;
  }
  .company-label {
    position: absolute;
    right: 22px;
    top: 184px;
    font-size: 12px;
    font-weight: 400;
    letter-spacing: 0.3px;
    color: var(--label-blue);
    text-transform: uppercase;
  }
  .rule {
    position: absolute;
    height: 4px;
    background: var(--rule);
  }
  .rule--upper { left: 300px; right: 22px; top: 204px; }
  .rule--lower { left: 22px; width: 400px; top: 266px; }
  .holder-name {
    position: absolute;
    left: 22px;
    top: 212px;
    font-size: 44px;
    line-height: 50px;
    color: var(--ink-soft);
    font-weight: 300;
    letter-spacing: -0.5px;
  }
  .holder-name .surname { color: var(--ink-dark); font-weight: 700; }
  .contact {
    position: absolute;
    font-size: 11.5px;
    line-height: 18px;
    color: var(--ink-dark);
    white-space: nowrap;
  }
  .contact .key { color: var(--label-blue); }
  .contact--address { left: 24px; top: 276px; }
  .contact--email { left: 276px; top: 276px; }
  .contact--web { right: 22px; top: 226px; }
</style>
</head>
<body>
<main class="stage">
  <article class="card">
    <header class="brand-tab">
      <span class="brand-name">Harlow Sun and Electrical</span>
    </header>

    <p class="company-label">Harlow Sun and Electrical</p>
    <div class="rule rule--upper"></div>

    <h1 class="holder-name">Dorian <span class="surname">Harlow</span></h1>
    <div class="rule rule--lower"></div>

    <p class="contact contact--web"><span class="key">Website:</span> www.hwx-example.net.nz</p>
    <p class="contact contact--address">
      <span class="key">Address:</span> 88 Meridian Street, 12th floor, NY USA<br>
      <span class="key">Phone:</span> 000 . 0274 . 69318
    </p>
    <p class="contact contact--email"><span class="key">Email:</span> dorian@hwx-example.net.nz</p>
  </article>
</main>
</body>
</html>
```